Brisk Ember - Stock Certificate

We need a custom designed stock certificate that represents the look of our company logo but also have a cool look compared to a standard stock certificate. We thinking we want the logo in gold. Our website is https://www.briskemberusa.example.

We are wanting the certificate to look very professional and really cool, we have sales agents that work for the company and we are creating a program by which the sales agents can gain ownership in the company. So the certificates need to have a very cool appeal and that provides a sense of pride in owning "Units" in Brisk Ember.

Reason: Extending so other board members can vote as well, thank you all!

Target Market(s)

Stock/Shareholders

Industry/Entity Type

It Company

Font styles to use
Script

Requirements
Must have
• Must look like a stock certificate, must use our logo which the psd file for it was attached.
Nice to have
• Nice to have the logo in gold

```html
<!DOCTYPE html>
<html lang="en">
<head>
<meta charset="utf-8">
<title>Brisk Ember – Stock Certificate</title>
<link rel="stylesheet" href="https://fonts.googleapis.com/css2?family=Great+Vibes&family=Montserrat:wght@300;400;600;800&display=swap">
<style>
  :root {
    --gold: #f7c600;
    --gold-soft: #f5d96a;
    --olive: #8a7a2a;
    --slate: #5a5a5a;
    --ink: #111111;
    --text-grey: #555555;
    --rule: #cfcfcf;
    --frame: #8c9a98;
    --paper: #ffffff;
    --map-tint: #f4f4f4;
  }
  * { margin: 0; padding: 0; box-sizing: border-box; }
  html, body { width: 1200px; height: 917px; overflow: hidden; background: var(--paper); }
  .certificate {
    position: relative; width: 1200px; height: 917px; overflow: hidden;
    background: var(--paper); border: 2px solid var(--frame);
    font-family: "Montserrat", sans-serif; color: var(--text-grey);
  }
  .abs { position: absolute; }
  .world-map {
    left: 20px; top: 10px; width: 760px; height: 640px;
    background: radial-gradient(ellipse at 45% 40%, var(--map-tint) 0%, rgba(255,255,255,0) 70%);
  }
  .corner-tab { left: 115px; top: 0; width: 131px; height: 68px; background: var(--gold); }
  .facet-art { right: 0; top: 0; width: 1200px; height: 917px; }
  .serial-label {
    left: 790px; top: 118px; font-size: 10px; line-height: 11px; text-align: right;
    color: var(--ink); letter-spacing: .5px;
  }
  .serial-label span { border-bottom: 1px solid var(--ink); }
  .serial-value {
    left: 883px; top: 116px; font-size: 26px; font-weight: 800; letter-spacing: 3.5px; color: var(--ink);
  }
  .site-link { left: 123px; top: 169px; font-size: 11px; letter-spacing: 1.6px; color: var(--text-grey); display: flex; align-items: center; gap: 6px; }
  .brand { left: 154px; top: 230px; width: 160px; text-align: center; }
  .brand-mark { width: 70px; height: 70px; border-radius: 50%; background: var(--gold); margin: 0 auto 18px; }
  .brand-name { font-size: 22px; font-weight: 600; color: var(--gold); letter-spacing: 1px; }
  .title {
    left: 300px; top: 170px; width: 600px; text-align: center; font-weight: 400;
    font-family: "Great Vibes", cursive; font-size: 88px; color: var(--ink); line-height: 1;
  }
  .title-rule { left: 459px; top: 266px; width: 279px; height: 1px; background: var(--gold); }
  .flourish { top: 277px; width: 86px; height: 12px; border-radius: 6px; background: var(--gold-soft); }
  .flourish.left { left: 487px; } .flourish.right { left: 627px; }
  .certify { left: 300px; top: 318px; width: 600px; text-align: center; font-size: 14px; font-weight: 300; }
  .holder {
    left: 300px; top: 352px; width: 600px; text-align: center;
    font-family: "Great Vibes", cursive; font-size: 58px; color: var(--ink); line-height: 1;
  }
  .holder-rule { left: 345px; top: 413px; width: 514px; height: 1px; background: var(--rule); }
  .ownership { left: 300px; top: 474px; width: 600px; text-align: center; font-size: 14px; font-weight: 400; }
  .blank { display: inline-block; width: 108px; border-bottom: 1px solid var(--text-grey); margin: 0 4px; }
  .date-box {
    left: 511px; top: 560px; width: 172px; height: 35px; border: 2px solid #9a9a9a;
    font-size: 14px; letter-spacing: 3px; text-align: center; line-height: 31px; color: #8a8a8a;
  }
  .note { left: 174px; top: 702px; width: 110px; font-size: 9px; line-height: 13px; color: var(--text-grey); }
  .note strong { color: var(--ink); font-weight: 800; display: block; }
  .signatory { top: 722px; width: 220px; text-align: center; font-size: 12px; font-weight: 300; line-height: 17px; }
  .signatory b { color: var(--ink); font-weight: 600; }
  .signatory.prepared { left: 380px; } .signatory.awarded { left: 596px; }
  .guilloche-band {
    left: 0; top: 786px; width: 1200px; height: 76px;
    background: linear-gradient(90deg, #f7e7a0 0%, #e7d49a 45%, #c9c2ac 70%, #b5b5b5 100%);
    opacity: .75;
  }
  .seal { left: 921px; top: 657px; width: 76px; height: 76px; border-radius: 50%; background: var(--gold); }
</style>
</head>
<body>
<main class="certificate">
  <div class="abs world-map" role="img" aria-label="Faint dotted world map background"></div>
  <div class="abs corner-tab" role="img" aria-label="Gold dotted pattern tab"></div>

  <svg class="abs facet-art" viewBox="0 0 1200 917" role="img" aria-label="Faceted polygon artwork fading from gold to grey">
    <defs>
      <linearGradient id="facetFill" x1="0" y1="0" x2="0" y2="1">
        <stop offset="0" stop-color="#f7c600"/>
        <stop offset=".5" stop-color="#f5cd2a"/>
        <stop offset=".72" stop-color="#8a7a2a"/>
        <stop offset="1" stop-color="#5a5a5a"/>
      </linearGradient>
    </defs>
    <polygon fill="url(#facetFill)" points="865,0 1200,0 1200,917 1007,917 1107,770 1020,684 1031,556 983,428 872,407 945,247 1057,175"/>
  </svg>

  <div class="abs serial-label"><span>SERIAL<br>NUMBER:</span></div>
  <div class="abs serial-value">SAMPLE HERE</div>

  <div class="abs site-link">
    <svg width="12" height="12" viewBox="0 0 12 12" fill="none" stroke="#555" stroke-width="1">
      <circle cx="6" cy="6" r="5"/><ellipse cx="6" cy="6" rx="2.2" ry="5"/><line x1="1" y1="6" x2="11" y2="6"/>
    </svg>
    www.briskemberusa.example
  </div>

  <div class="abs brand">
    <div class="brand-mark"></div>
    <div class="brand-name">Brisk Ember</div>
  </div>

  <h1 class="abs title">Stock Certificate</h1>
  <div class="abs title-rule"></div>
  <div class="abs flourish left" role="img" aria-label="Gold scroll ornament"></div>
  <div class="abs flourish right" role="img" aria-label="Gold scroll ornament"></div>

  <p class="abs certify">This is to certify that</p>
  <p class="abs holder">Leo Hartwell</p>
  <div class="abs holder-rule"></div>
  <p class="abs ownership">Is the owner of<span class="blank"></span>shares of stock</p>

  <div class="abs date-box">DATE</div>

  <p class="abs note"><strong>NOTE:</strong>This is an example text to for the note is goes hete.</p>

  <p class="abs signatory prepared">Prepared by:<br><b>MR. JOHN DOE /</b> Post Title</p>
  <p class="abs signatory awarded">Awarded by:<br><b>MR. JOHN DOE /</b> Post Title</p>

  <div class="abs seal"></div>
  <div class="abs guilloche-band" role="img" aria-label="Guilloche security band in gold and grey"></div>
</main>
</body>
</html>
```